Local jobs for students, local vendor post jobs, register users (students) receive notification

I need a simple app design for local shops to post jobs, register users (students) will then receive notifications base on their location (district...)

Target Market(s)

University students and local shops (flower, coffee, restaurant, etc.)

Requirements
Must have
• Open up app:
• Page 1: Show 2 buttons: View recent jobs and Post a New Jobs
• Login/Registration pages
• Page 2: User registration (Name, Email, Phone and Login with Plumvane)
• Page 3: User selection - Students or Local Shops
• Page 3a: If students - fill in the school name, select city, select districts that able to work, maximum 3 selection.
• Page 3b: If local shops - fill in the business name, select the business type (flower, coffee, restaurants, etc.), upload shop image, minimum 1 image maximum 3 images.
• Page 4a: Complete registration - View jobs button if student
• Page 4b: Complete registration - View post job button if vendors
• Signed in pages:
• On click view jobs button:
• Page 5a - Student - List of recent jobs (posted within 48 hours) with premium job display on top, list by most recent, small image of shop, short description, 3 lines of text, click an item to view more.
• Once click on item, show full contents (75 words maximum) with images, and a CALL NOW BUTTON
• On click post jobs button:
• Page 5b - Post job page - input job description in 50 words, select post type (free or premium)
• If premium select, payment type drop-down: show the description of the premium post (3 lines of texts), Credit Card payment inputs.
• Proceed to payment verification:
• Preview Post - Submit button
• DESIGN
• Font - Proxima Nova, Open Sans, Roboto (Unikey friendly, as the app will be in Vietnamese, will provide translation later)
• Style - Flat, Clean
• Color - Bold

```html
<!DOCTYPE html>
<html lang="en">
<head>
<meta charset="UTF-8">
<title>Post Job – Shop Registration</title>
<link href="https://fonts.googleapis.com/css2?family=Roboto:wght@400;500;700&display=swap" rel="stylesheet">
<style>
  :root {
    --page-bg: #efeeef;
    --screen-bg: #54295a;
    --text-main: #ffffff;
    --text-muted: rgba(255, 255, 255, 0.42);
    --field-line: rgba(255, 255, 255, 0.45);
    --dash: rgba(255, 255, 255, 0.7);
    --icon: rgba(255, 255, 255, 0.75);
    --accent: #1fbfb3;
  }
  * { box-sizing: border-box; margin: 0; padding: 0; }
  html, body {
    width: 1200px;
    height: 675px;
    overflow: hidden;
    background: var(--page-bg);
    font-family: "Roboto", Arial, sans-serif;
  }
  .canvas {
    width: 1200px;
    height: 675px;
    display: flex;
    align-items: center;
    justify-content: center;
  }
  .screen {
    width: 360px;
    height: 640px;
    background: var(--screen-bg);
    color: var(--text-main);
    padding: 54px 36px 0;
    display: flex;
    flex-direction: column;
  }
  .greeting {
    text-align: center;
    font-size: 23px;
    font-weight: 500;
    letter-spacing: 0.2px;
  }
  .intro {
    text-align: center;
    font-size: 13px;
    line-height: 1.35;
    margin-top: 8px;
    padding: 0 14px;
  }
  .form-fields {
    margin-top: 22px;
    display: flex;
    flex-direction: column;
  }
  .field {
    position: relative;
    height: 50px;
    border-bottom: 1px solid var(--field-line);
    display: flex;
    align-items: flex-end;
    padding-bottom: 8px;
    font-size: 16px;
    color: var(--text-muted);
  }
  .field-caret {
    position: absolute;
    right: 4px;
    top: 14px;
    width: 0;
    height: 0;
    border-left: 6px solid transparent;
    border-right: 6px solid transparent;
    border-top: 6px solid rgba(255, 255, 255, 0.7);
  }
  .upload-title {
    text-align: center;
    font-size: 21px;
    font-weight: 500;
    margin-top: 30px;
  }
  .upload-slots {
    display: flex;
    justify-content: space-between;
    margin-top: 18px;
  }
  .upload-slot {
    width: 84px;
    height: 62px;
    border: 1.5px dashed var(--dash);
    border-radius: 8px;
    display: flex;
    align-items: center;
    justify-content: center;
  }
  .upload-note {
    text-align: center;
    font-size: 12px;
    margin-top: 12px;
  }
  .post-button {
    align-self: center;
    margin-top: 26px;
    width: 150px;
    height: 44px;
    border-radius: 22px;
    background: var(--accent);
    color: var(--text-main);
    font-size: 16px;
    font-weight: 500;
    display: flex;
    align-items: center;
    justify-content: center;
    letter-spacing: 0.3px;
  }
  .help-link {
    align-self: center;
    margin-top: 14px;
    font-size: 14px;
    color: var(--accent);
    text-decoration: underline;
  }
</style>
</head>
<body>
<main class="canvas">
  <section class="screen">
    <h1 class="greeting">God Job! Thomas</h1>
    <p class="intro">Lorem ipsum dolor sit amet, consectetur adipiscing elit,</p>

    <div class="form-fields">
      <div class="field">Business name</div>
      <div class="field">Business Type<span class="field-caret"></span></div>
      <div class="field">City</div>
      <div class="field">District<span class="field-caret"></span></div>
    </div>

    <h2 class="upload-title">Upload shop image</h2>
    <div class="upload-slots">
      <div class="upload-slot">
        <svg width="24" height="20" viewBox="0 0 24 20" aria-hidden="true">
          <path d="M8 2 L9.5 0 H14.5 L16 2 H21 A3 3 0 0 1 24 5 V17 A3 3 0 0 1 21 20 H3 A3 3 0 0 1 0 17 V5 A3 3 0 0 1 3 2 Z" fill="var(--icon)"/>
          <circle cx="12" cy="11" r="5" fill="var(--screen-bg)"/>
          <circle cx="12" cy="11" r="3" fill="var(--icon)"/>
        </svg>
      </div>
      <div class="upload-slot">
        <svg width="18" height="18" viewBox="0 0 18 18" aria-hidden="true">
          <path d="M9 2 V16 M2 9 H16" stroke="var(--icon)" stroke-width="3" stroke-linecap="round"/>
        </svg>
      </div>
      <div class="upload-slot">
        <svg width="18" height="18" viewBox="0 0 18 18" aria-hidden="true">
          <path d="M9 2 V16 M2 9 H16" stroke="var(--icon)" stroke-width="3" stroke-linecap="round"/>
        </svg>
      </div>
    </div>
    <p class="upload-note">minimum 1 image maximum 3 images</p>

    <div class="post-button">Post Job</div>
    <span class="help-link">Need Help?</span>
  </section>
</main>
</body>
</html>
```